Book Cover - Life Lessons Book

I have written a book for my sons who are graduating high school and college. Working title is "Chart Your Compass.....38 Lessons Learned at Home" I am looking for the book to appeal to young adults and parents who would want to give this book to them. It is a 125 page book that will be hardback and paperback - probably 5x8 or 6x9.
Updates

Reason: Altered some of the design elements based on the first submissions received. Would really like to have designs by Monday, May 15, 2016 but could not force a 2 day extension.

Target Market(s)

Young adults -- graduates, 20-3- year olds. And, parents would would give a book to their kids

Industry/Entity Type

Book Publisher

Font styles to use
Serif

Requirements
Must have
• Great design. It is a book cover so needs to catch the attention.
Nice to have
• I am open to more animated/playful/modern look or a more traditional look. Just would like to appeal to young adults and parents.
Should not have
• Anything in poor taste

```html
<!DOCTYPE html>
<html lang="en">
<head>
<meta charset="utf-8">
<title>Chart Your Compass – Book Cover</title>
<link rel="stylesheet" href="https://fonts.googleapis.com/css2?family=Oswald:wght@400;500&family=Nothing+You+Could+Do&display=swap">
<style>
  :root {
    --page-bg: #ffffff;
    --paper: #f2e8cf;
    --paper-edge: #e3d3ac;
    --teal: #1e6581;
    --teal-deep: #185770;
    --ink-cream: #f5edd6;
    --accent-orange: #d8862a;
  }
  * { margin: 0; padding: 0; box-sizing: border-box; }
  html, body {
    width: 1016px;
    height: 1200px;
    overflow: hidden;
    background: var(--page-bg);
  }
  .canvas {
    position: relative;
    width: 1016px;
    height: 1200px;
  }
  .cover {
    position: absolute;
    left: 138px;
    top: 40px;
    width: 740px;
    height: 1120px;
    background: var(--paper);
    box-shadow: inset 0 0 0 3px var(--paper-edge);
  }
  .cover-panel {
    position: absolute;
    left: 28px;
    top: 30px;
    right: 26px;
    bottom: 34px;
    background: radial-gradient(ellipse at 50% 40%, var(--teal) 0%, var(--teal-deep) 100%);
    clip-path: polygon(0 1%, 6% 0, 22% 0.6%, 40% 0, 63% 0.5%, 85% 0, 100% 0.8%, 99.4% 20%, 100% 45%, 99.3% 70%, 100% 99%, 80% 100%, 55% 99.4%, 30% 100%, 8% 99.5%, 0.4% 100%, 0 75%, 0.8% 50%, 0 25%);
    color: var(--ink-cream);
    font-family: "Oswald", "Arial Narrow", sans-serif;
    text-transform: uppercase;
  }
  .title {
    position: absolute;
    top: 42px;
    left: 0;
    right: 0;
    text-align: center;
    font-weight: 400;
    font-size: 128px;
    line-height: 1.12;
    letter-spacing: 1px;
  }
  .lesson-count {
    position: absolute;
    top: 366px;
    left: 0;
    right: 0;
    text-align: center;
    font-weight: 500;
    font-size: 104px;
    line-height: 1;
  }
  .subtitle {
    position: absolute;
    top: 560px;
    left: 52px;
    font-weight: 400;
    font-size: 72px;
    line-height: 1;
    white-space: nowrap;
  }
  .circled {
    position: relative;
    display: inline-block;
  }
  .circled-mark {
    position: absolute;
    left: -26px;
    top: -26px;
    width: calc(100% + 52px);
    height: calc(100% + 52px);
    overflow: visible;
  }
  .signature {
    position: absolute;
    top: 700px;
    right: 70px;
    font-family: "Nothing You Could Do", cursive;
    text-transform: none;
    font-size: 150px;
    line-height: 1;
    color: var(--ink-cream);
  }
  .signature-underline {
    position: absolute;
    left: 250px;
    top: 880px;
    width: 380px;
    height: 50px;
    overflow: visible;
  }
</style>
</head>
<body>
<div class="canvas">
  <div class="cover">
    <div class="cover-panel">
      <h1 class="title">Chart Your<br>Compass</h1>
      <div class="lesson-count">38</div>
      <div class="subtitle">
        <span class="circled">Lessons
          <svg class="circled-mark" viewBox="0 0 300 130" preserveAspectRatio="none" aria-hidden="true">
            <path d="M150 6 C 240 4, 296 30, 294 66 C 292 104, 230 126, 148 124 C 66 122, 6 102, 8 64 C 10 30, 70 8, 160 10 C 200 11, 220 14, 236 20"
                  fill="none" stroke="var(--accent-orange)" stroke-width="6" stroke-linecap="round"/>
          </svg>
        </span> Learned At
      </div>
      <div class="signature">Home</div>
      <svg class="signature-underline" viewBox="0 0 380 50" aria-hidden="true">
        <path d="M4 42 C 120 30, 250 16, 376 6" fill="none" stroke="var(--accent-orange)" stroke-width="8" stroke-linecap="round"/>
      </svg>
    </div>
  </div>
</div>
</body>
</html>
```